Brasko Construction Business Card

I need a business card design for my company.
We are a construction/machinery company.
I would like to see my logo on the front of the card and my details on the other side
I would like the card to be black or dark grey in colour,with my logo as i send it or modified with a lighter blue colour
I would like to see the design kept fairly simple,but eye catching at the same time
Industry/Entity Type
Business
Contact Information for Business Card
Name
Phone Number
Address
Email
Colors
00a990
1b1b1b
000000
474747
ececec

```html
<!DOCTYPE html>
<html lang="en">
<head>
<meta charset="utf-8">
<title>Brasko Construction Business Card</title>
<link rel="stylesheet" href="https://fonts.googleapis.com/css2?family=Cinzel:wght@400;700&display=swap">
<style>
  :root {
    --teal: #00a990;
    --card: #1b1b1b;
    --card-edge: #474747;
    --ink-light: #ececec;
    --backdrop: #d9d9d9;
    --shadow: rgba(0, 0, 0, 0.35);
  }
  * { box-sizing: border-box; margin: 0; padding: 0; }
  html, body {
    width: 1200px;
    height: 900px;
    overflow: hidden;
    background: var(--backdrop);
    font-family: "Cinzel", serif;
  }
  .canvas {
    position: relative;
    width: 1200px;
    height: 900px;
  }
  .card {
    position: absolute;
    left: 250px;
    width: 700px;
    height: 400px;
    background: var(--card);
    border: 1px solid var(--card-edge);
    box-shadow: 0 12px 28px var(--shadow);
  }
  .card--details { top: 30px; }
  .card--brand { top: 470px; }

  /* Details side */
  .identity {
    position: absolute;
    right: 360px;
    top: 150px;
    text-align: right;
  }
  .identity__name {
    color: var(--ink-light);
    font-size: 19px;
    letter-spacing: 1.5px;
  }
  .identity__role {
    color: var(--teal);
    font-size: 17px;
    letter-spacing: 1.5px;
    margin-top: 8px;
  }
  .divider {
    position: absolute;
    left: 350px;
    top: 110px;
    width: 3px;
    height: 160px;
    background: var(--teal);
  }
  .contact {
    position: absolute;
    left: 380px;
    top: 112px;
    list-style: none;
    color: var(--ink-light);
    font-size: 15px;
    letter-spacing: 1px;
    line-height: 1.15;
  }
  .contact li + li { margin-top: 22px; }

  /* Brand side */
  .brand {
    position: absolute;
    inset: 0;
    display: flex;
    align-items: center;
    justify-content: center;
    gap: 18px;
  }
  .brand__mark {
    width: 34px;
    height: 34px;
    background: var(--ink-light);
  }
  .brand__name {
    color: var(--ink-light);
    font-size: 42px;
    font-weight: 700;
    letter-spacing: 3px;
    text-transform: uppercase;
  }
</style>
</head>
<body>
<main class="canvas">
  <section class="card card--details" aria-label="Card back with contact details">
    <div class="identity">
      <p class="identity__name">Daniel Brasko</p>
      <p class="identity__role">Director</p>
    </div>
    <div class="divider"></div>
    <ul class="contact">
      <li>DANIEL@BRASKOBUILD.COM</li>
      <li>+123 555 014 20</li>
      <li>57 HARBOR LANE FAIRVIEW<br>TAMPA FL 33601 USA</li>
    </ul>
  </section>

  <section class="card card--brand" aria-label="Card front with company name">
    <div class="brand">
      <span class="brand__mark"></span>
      <p class="brand__name">Brasko Construction</p>
    </div>
  </section>
</main>
</body>
</html>
```